Brambleton Resource Holdings, LP Letter Head

We need an official company letter head design that is clean and mimics our company logo style. It will include our logo, address, phone, and website. We are an OIl and Gas mineral purchasing company, so hints of oil rigs or related design would be desirable.

Industry/Entity Type

Oil And Gas

Colors
ec1f27
f04a50
f59195
fbd4d5

Requirements
Must have
• Logo
• 7392 Whitcombe R. Ashdale Parkway, Suite 618
• Dallas TX, 75391
• 214-673-1958
• www.bramblestoneres.example
Nice to have
• Oil Rigs or OIl and gas related design

```html
<!DOCTYPE html>
<html lang="en">
<head>
<meta charset="utf-8">
<title>Brambleton Resource Holdings, LP — Letterhead</title>
<link rel="stylesheet" href="https://fonts.googleapis.com/css2?family=PT+Sans:wght@400;700&family=Great+Vibes&display=swap">
<style>
  :root {
    --brand-red: #ec1f27;
    --brand-red-soft: #f04a50;
    --charcoal: #3f3f41;
    --text-gray: #4a4a4a;
    --heading-gray: #444446;
    --backdrop: #b3b3b3;
    --paper: #ffffff;
  }
  * { margin: 0; padding: 0; box-sizing: border-box; }
  html, body {
    width: 985px; height: 1200px; overflow: hidden;
    background: var(--backdrop);
    font-family: "PT Sans", Arial, sans-serif;
  }
  .letterhead {
    position: absolute; left: 85px; top: 78px;
    width: 815px; height: 1044px;
    background: var(--paper);
    overflow: hidden;
  }
  .brand {
    position: absolute; left: 83px; top: 82px; width: 220px;
    text-align: center;
  }
  .brand-mark {
    display: block; width: 73px; height: 73px; margin: 0 auto 10px;
    background: var(--brand-red);
  }
  .brand-name {
    color: var(--brand-red); font-weight: 400; font-size: 21px; line-height: 24px;
  }
  .contact {
    position: absolute; right: 80px; top: 107px;
    text-align: right; font-size: 10.5px; line-height: 14px;
    color: #333; font-weight: 700;
  }
  .contact .address { margin-bottom: 10px; }
  .contact-line { display: flex; justify-content: flex-end; align-items: center; gap: 6px; }
  .contact-line svg { width: 9px; height: 9px; flex: none; }
  .letter-body {
    position: absolute; left: 82px; top: 298px; width: 656px;
    color: var(--text-gray);
  }
  .letter-title {
    font-size: 17.5px; font-weight: 700; color: var(--heading-gray);
    margin-bottom: 16px;
  }
  .letter-body p {
    font-size: 12.6px; line-height: 16.9px;
    text-align: justify; hyphens: auto;
    margin-bottom: 16.9px;
  }
  .letter-body p.truncated { height: 67.6px; overflow: hidden; }
  .signature {
    position: absolute; right: 78px; top: 866px;
    font-family: "Great Vibes", cursive; font-size: 28px; color: #555;
  }
  .rig-illustration {
    position: absolute; left: 82px; top: 877px; width: 87px; height: 121px;
    background: linear-gradient(180deg, var(--brand-red-soft) 0%, var(--brand-red) 100%);
  }
  .footer-bands { position: absolute; left: 0; top: 998px; width: 815px; height: 46px; }
</style>
</head>
<body>
  <main class="letterhead">
    <header>
      <div class="brand">
        <span class="brand-mark"></span>
        <div class="brand-name">Brambleton Resource Holdings, LP</div>
      </div>
      <address class="contact" style="font-style:normal">
        <div class="address">7392 Whitcombe R. Ashdale Parkway,<br>Suite 618, Dallas TX, 75391</div>
        <div class="contact-line">214-673-1958
          <svg viewBox="0 0 10 10" aria-hidden="true"><path d="M2 0.5 L3.8 2.6 L2.9 3.8 Q4 6 6.2 7.1 L7.4 6.2 L9.5 8 L8.2 9.5 Q4.5 9.3 2 6.8 Q0.3 4.4 0.6 1.6 Z" fill="var(--brand-red)"/></svg>
        </div>
        <div class="contact-line">www.bramblestoneres.example
          <svg viewBox="0 0 10 10" aria-hidden="true"><circle cx="5" cy="5" r="4.5" fill="var(--brand-red-soft)"/><path d="M0.5 5h9M5 0.5v9M2 2.5q3 1.5 6 0M2 7.5q3-1.5 6 0" stroke="#fff" stroke-width="0.6" fill="none"/></svg>
        </div>
      </address>
    </header>

    <section class="letter-body">
      <h1 class="letter-title">Lorem ipsum dolor sit amet</h1>
      <p>Lorem ipsum dolor sit amet, consectetur adipiscing elit, sed do eiusmod tempor incididunt ut labore et dolore magna aliqua. Ut enim ad minim veniam, quis nostrud exercitation ullamco laboris nisi ut aliquip ex ea commodo consequat. Duis aute irure dolor in reprehenderit in voluptate velit esse cillum dolore eu fugiat nulla pariatur. Excepteur sint occaecat cupidatat non proident, sunt in culpa qui officia deserunt mollit anim id est laborum Sed ut perspiciatis unde omnis iste natus error sit voluptatem accusantium doloremque laudantium, totam rem aperiam, eaque ipsa quae ab illo inventore veritatis et quasi architecto beatae vitae dicta sunt explicabo. Nemo enim ipsam voluptatem quia voluptas sit aspernatur aut odit aut fugit, sed quia consequuntur magni dolores eos qui ratione voluptatem sequi nesciunt. Neque porro quisquam est, qui dolorem ipsum quia dolor sit amet, consectetur, adipisci velit, sed quia non numquam eius modi tempora incidunt ut labore et dolore magnam aliquam quaerat voluptatem. Ut enim ad minima veniam, quis nostrum exercitationem ullam corporis suscipit laboriosam, nisi ut aliquid ex ea commodi consequatur? Quis autem vel eum iure reprehenderit qui in ea voluptate velit esse quam nihil molestiae consequatur, vel illum qui dolorem eum fugiat quo voluptas nulla pariatur?</p>
      <p>Lorem ipsum dolor sit amet, consectetur adipiscing elit, sed do eiusmod tempor incididunt ut labore et dolore magna aliqua. Ut enim ad minim veniam, quis nostrud exercitation ullamco laboris nisi ut aliquip ex ea commodo consequat. Duis aute irure dolor in reprehenderit in voluptate velit esse cillum dolore eu fugiat nulla pariatur. Excepteur sint occaecat cupidatat non proident, sunt in culpa qui officia deserunt mollit anim id est laborum Sed ut perspiciatis unde omnis iste natus error sit voluptatem accusantium doloremque laudantium, totam rem aperiam, eaque ipsa quae ab illo inventore veritatis et quasi architecto beatae vitae dicta sunt explicabo. Nemo enim ipsam voluptatem quia voluptas sit aspernatur aut odit aut fugit, sed quia consequuntur magni dolores eos qui ratione voluptatem sequi nesciunt. Neque porro quisquam est, qui dolorem ipsum quia dolor sit amet, consectetur, adipisci velit, sed quia non numquam eius modi tempora incidunt ut labore et dolore magnam aliquam quaerat voluptatem. Ut enim ad minima veniam, quis nostrum exercitationem ullam corporis suscipit laboriosam, nisi ut aliquid ex ea commodi consequatur? Quis autem vel eum iure reprehenderit qui in ea voluptate velit esse quam nihil molestiae consequatur, vel illum qui dolorem eum fugiat quo voluptas nulla pariatur?</p>
      <p class="truncated">Lorem ipsum dolor sit amet, consectetur adipiscing elit, sed do eiusmod tempor incididunt ut labore et dolore magna aliqua. Ut enim ad minim veniam, quis nostrud exercitation ullamco laboris nisi ut aliquip ex ea commodo consequat. Duis aute irure dolor in reprehenderit in voluptate velit esse cillum dolore eu fugiat nulla pariatur. Excepteur sint occaecat cupidatat non proident, sunt in culpa qui officia deserunt mollit anim id est laborum Sed ut perspiciatis unde omnis iste natus error sit voluptatem.</p>
    </section>

    <div class="signature">Signature</div>

    <div class="rig-illustration" role="img" aria-label="Red silhouette of an offshore oil rig with derrick, crane and flare"></div>

    <svg class="footer-bands" viewBox="0 0 815 46" aria-hidden="true">
      <polygon points="0,0 565,0 557,46 0,46" fill="var(--brand-red)"/>
      <polygon points="575,0 815,0 815,46 567,46" fill="var(--charcoal)"/>
    </svg>
  </main>
</body>
</html>
```